Email Banner for Technology Company

We need a new email banner. The purpose of the email banner is to make us look more professional as a business and keep all communications with clients uniform. The previous designs which we have included below have now become outdated as our brand has developed and we need the new banner to become more aligned and modern.

We are a marketing organization that specialises in lead generation, email newsletters are sent to prospects on a regular basis. Therefore, it is important that we have an aesthetically pleasing banner as this is the first real impression prospects have our business. First impressions matter.

We are looking for a new email banner design as the current design is now outdated and does not reflect who we are as a business.

The new banners are required for launch at the start of Q2.

There is future work in the pipeline for the winning design. We have multiple industry sites that will require the new design as well as creating each of these in multiple languages.

The design must include the Zentroval wording the tagline 'The Ultimate Research Library for Technology Pro's.
It needs to be creative and fun but still remain professional, sticking with the colour theme that already exists.

Requirements
Must have
• The design must include the Zentroval wording the tagline 'The Ultimate Research Library for Technology Pro's.

```html
<!DOCTYPE html>
<html lang="en">
<head>
<meta charset="utf-8">
<title>Zentroval Email Banner Concepts</title>
<link rel="stylesheet" href="https://fonts.googleapis.com/css2?family=Montserrat:wght@400;500;600;700&display=swap">
<style>
  :root {
    --board-mid: #474747;
    --board-edge: #242424;
    --teal-deep: #083f52;
    --teal-mid: #0b5a72;
    --teal-bright: #0f7d9c;
    --sky: #6fd0f5;
    --sky-strong: #3cbfe9;
    --paper: #f2f2f2;
    --navy: #1f3a52;
    --white: #ffffff;
    --ink-teal: #0d4a5a;
  }
  * { margin: 0; padding: 0; box-sizing: border-box; }
  html, body { width: 1200px; height: 787px; overflow: hidden; }
  body {
    font-family: "Montserrat", Arial, sans-serif;
    background: radial-gradient(ellipse at 50% 45%, var(--board-mid) 0%, #363636 45%, var(--board-edge) 100%);
    position: relative;
  }
  .concept-number {
    position: absolute;
    left: 50px;
    color: var(--white);
    font-weight: 700;
    font-size: 19px;
  }
  .banner {
    position: absolute;
    left: 45px;
    width: 1096px;
    height: 183px;
    overflow: hidden;
    box-shadow: 0 14px 30px rgba(0,0,0,.55);
  }
  .banner-bg { position: absolute; inset: 0; width: 100%; height: 100%; display: block; }
  .brand-name {
    position: absolute;
    color: var(--sky);
    font-weight: 600;
    font-size: 40px;
    letter-spacing: -0.5px;
    line-height: 1;
  }
  .tagline {
    position: absolute;
    color: var(--white);
    font-weight: 400;
    font-size: 24.5px;
    letter-spacing: 0.4px;
    white-space: nowrap;
    line-height: 1;
  }
  .tagline strong { font-weight: 700; }
  .tagline .accent { color: var(--sky-strong); font-weight: 500; }
  .cta {
    position: absolute;
    width: 188px;
    height: 46px;
    display: flex;
    align-items: center;
    justify-content: center;
    font-size: 24px;
    font-weight: 600;
    text-decoration: none;
  }
  /* Concept 1 */
  .banner--rings { top: 60px; }
  .banner--rings .brand-name { left: 88px; top: 72px; }
  .banner--rings .tagline { left: 373px; top: 82px; }
  .banner--rings .cta {
    left: 893px; top: 0;
    background: var(--white);
    color: var(--ink-teal);
    border-radius: 0 0 46px 46px;
    font-weight: 500;
  }
  /* Concept 2 */
  .banner--wave { top: 298px; }
  .banner--wave .brand-name { left: 56px; top: 80px; }
  .banner--wave .tagline { left: 319px; top: 86px; }
  .banner--wave .cta {
    left: 893px; top: 0;
    background: var(--navy);
    color: var(--white);
    border-radius: 0 0 46px 46px;
  }
  /* Concept 3 */
  .banner--chevron { top: 536px; }
  .banner--chevron .brand-name { left: 94px; top: 80px; }
  .banner--chevron .tagline { left: 419px; font-size: 27px; }
  .banner--chevron .tagline.line-one { top: 62px; }
  .banner--chevron .tagline.line-two { top: 102px; }
  .banner--chevron .cta {
    left: 908px; top: 137px;
    background: var(--navy);
    color: var(--white);
    border-radius: 30px 0 0 0;
  }
</style>
</head>
<body>

  <span class="concept-number" style="top:33px">1.</span>
  <section class="banner banner--rings">
    <svg class="banner-bg" viewBox="0 0 1096 183" preserveAspectRatio="none" role="img" aria-label="Teal background with soft concentric rings">
      <defs>
        <linearGradient id="ringsFill" x1="0" y1="0" x2="1" y2="1">
          <stop offset="0" stop-color="#0a4b60"/>
          <stop offset="0.5" stop-color="#093f53"/>
          <stop offset="1" stop-color="#0c607a"/>
        </linearGradient>
      </defs>
      <rect width="1096" height="183" fill="url(#ringsFill)"/>
      <g fill="#0f7d9c">
        <circle cx="175" cy="210" r="245" opacity=".18"/>
        <circle cx="175" cy="210" r="195" opacity=".2"/>
        <circle cx="175" cy="210" r="145" opacity=".22"/>
        <circle cx="175" cy="210" r="100" opacity=".25"/>
        <circle cx="930" cy="20" r="250" opacity=".15"/>
        <circle cx="930" cy="20" r="200" opacity=".18"/>
        <circle cx="930" cy="20" r="145" opacity=".22"/>
        <circle cx="930" cy="20" r="95" opacity=".25"/>
      </g>
    </svg>
    <div class="brand-name">Zentroval</div>
    <p class="tagline">The Ultimate Research Library for <span class="accent">Technology Pro’s</span></p>
    <a class="cta" href="#">Click Here</a>
  </section>

  <span class="concept-number" style="top:272px">2.</span>
  <section class="banner banner--wave">
    <svg class="banner-bg" viewBox="0 0 1096 183" preserveAspectRatio="none" role="img" aria-label="Teal panel with a light sweeping curve">
      <defs>
        <linearGradient id="waveFill" x1="0" y1="0" x2="0" y2="1">
          <stop offset="0" stop-color="#0a4a60"/>
          <stop offset="1" stop-color="#0f7d9c"/>
        </linearGradient>
      </defs>
      <rect width="1096" height="183" fill="url(#waveFill)"/>
      <path d="M181 0 C 80 0 0 80 0 183 L 235 183 C 235 80 315 0 416 0 Z" fill="var(--paper)"/>
      <path d="M1096 0 L1096 183 L922 183 C 1020 183 1096 100 1096 0 Z" fill="var(--paper)"/>
    </svg>
    <div class="brand-name">Zentroval</div>
    <p class="tagline">The Ultimate Research Library for <strong>Technology Pro’s</strong></p>
    <a class="cta" href="#">Click Here</a>
  </section>

  <span class="concept-number" style="top:507px">3.</span>
  <section class="banner banner--chevron">
    <svg class="banner-bg" viewBox="0 0 1096 183" preserveAspectRatio="none" role="img" aria-label="Teal background with a dark chevron at the left">
      <defs>
        <linearGradient id="chevronFill" x1="0" y1="0" x2="1" y2="0">
          <stop offset="0" stop-color="#0a5068"/>
          <stop offset="1" stop-color="#0e7594"/>
        </linearGradient>
      </defs>
      <rect width="1096" height="183" fill="url(#chevronFill)"/>
      <polygon points="0,0 161,0 80,114 129,183 33,183 0,150" fill="#07394b" opacity=".7"/>
    </svg>
    <div class="brand-name">Zentroval</div>
    <p class="tagline line-one">The Ultimate Research Library for</p>
    <p class="tagline line-two"><strong>Technology Pro’s</strong></p>
    <a class="cta" href="#">Click Here</a>
  </section>

</body>
</html>
```